Brinewardsea.com Website design needed!!

We are looking for a website layout to match the attached logo. We specialize in Dive Charters and currently are located in the Virgin Islands off of St. Thomas. Please create a design that is compatible with Bootstrap and have the grid in mind. WE are looking for creative and extremely professional layout design.

Target Market(s)

Scuba Diving, Divers looking for a diving charter in the Virgin Islands.

Number of Pages Required

3 page

Font styles to use
Serif

Requirements
Must have
• Must be Bootstrap friendly.
• Must work with the logo we provided. Colors etc.

```html
<!DOCTYPE html>
<html lang="en">
<head>
<meta charset="utf-8">
<title>Brinewardsea – Charters and Scuba</title>
<link href="https://fonts.googleapis.com/css2?family=Open+Sans:ital,wght@0,400;0,600;0,700;0,800;1,400&display=swap" rel="stylesheet">
<style>
:root{
  --sea:#0d93e6;
  --sea-deep:#0a6fb0;
  --sea-light:#27a9f0;
  --red:#d9222e;
  --gold:#e0a52c;
  --ink:#444a52;
  --muted:#7b8088;
  --page:#eef3f7;
  --white:#ffffff;
}
*{margin:0;padding:0;box-sizing:border-box}
html,body{width:1200px;height:1164px;overflow:hidden}
body{font-family:'Open Sans',sans-serif;background:var(--page);position:relative;color:var(--ink)}
.hero-photo{position:absolute;left:0;top:0;width:1200px;height:700px;
  background:linear-gradient(180deg,#1aa2ee 0%,#1386cf 35%,#0c5f98 70%,#2b7fb6 100%);
  clip-path:polygon(0 0,100% 0,100% 694px,0 577px)}
.hero-photo .diver{position:absolute;left:250px;top:140px;width:560px;height:480px;
  background:radial-gradient(ellipse at center,rgba(20,30,45,.55),rgba(20,30,45,0) 70%)}
.page-fade{position:absolute;left:0;top:600px;width:1200px;height:492px;
  background:linear-gradient(180deg,rgba(238,243,247,0),var(--page) 25%)}
.brand{position:absolute;left:101px;top:34px;display:flex;align-items:center;gap:8px;
  font-weight:700;font-size:24px;color:var(--white)}
.brand .dot{width:22px;height:22px;border-radius:50%;background:var(--red)}
.call{position:absolute;right:99px;top:30px;display:flex;align-items:center;gap:16px;color:var(--white);font-size:17px}
.call b{font-size:20px;font-weight:700}
.call .ring{width:42px;height:42px;border-radius:50%;border:2px solid var(--gold);display:flex;align-items:center;justify-content:center}
.nav{position:absolute;left:99px;top:99px;width:1002px;height:37px;background:var(--red);display:flex;align-items:center}
.nav a{color:var(--white);text-decoration:none;font-size:13px;font-weight:600;margin-left:27px;margin-right:27px}
.nav .lang{margin-left:auto;height:100%;border-left:1px solid rgba(255,255,255,.3);width:74px;display:flex;align-items:center;justify-content:center;gap:8px}
.nav .flag{width:22px;height:14px;background:#27407a;border:1px solid #fff}
.arrow{position:absolute;top:305px;width:43px;height:43px;border-radius:50%;background:rgba(255,255,255,.35);display:flex;align-items:center;justify-content:center}
.arrow.left{left:28px}.arrow.right{right:26px;background:rgba(255,255,255,.15)}
.hero-title{position:absolute;left:99px;top:280px;color:var(--white);font-size:38px;font-weight:800;letter-spacing:.5px}
.hero-sub{position:absolute;left:99px;top:340px;color:var(--gold);font-size:15.5px;font-weight:700}
.search{position:absolute;left:804px;top:239px;width:297px;height:370px;background:rgba(23,150,230,.92);padding:22px 12px 24px 20px}
.search h2{color:var(--white);font-size:17.5px;font-weight:600;line-height:28px}
.radio{display:flex;align-items:center;gap:12px;color:var(--white);font-size:13.5px;margin-top:16px;padding-left:6px}
.radio:first-of-type{margin-top:18px}
.radio i{width:12px;height:12px;border-radius:50%;background:var(--white);display:flex;align-items:center;justify-content:center}
.radio i::after{content:"";width:6px;height:6px;border-radius:50%;background:#333}
.radio.on i::after{background:var(--red)}
.field{display:block;width:240px;height:34px;background:var(--white);margin:0 0 17px 5px;color:#999;font-size:13px;line-height:34px;padding-left:14px}
.field:first-of-type{margin-top:24px}
.btn-gold{display:inline-block;margin:8px 0 0 5px;width:165px;height:44px;background:var(--gold);color:var(--white);font-size:16px;font-weight:600;text-align:center;line-height:44px}
.welcome{position:absolute;left:99px;top:656px;width:470px}
.welcome h1{font-size:27px;font-weight:700;color:var(--sea)}
.welcome h1 span{color:var(--gold)}
.welcome .lead{margin-top:14px;color:var(--red);font-style:italic;font-size:12.5px;line-height:23px;width:420px}
.welcome p{margin-top:15px;color:var(--muted);font-size:12.5px;line-height:23px;letter-spacing:-.1px}
.btn-blue{position:absolute;left:99px;top:1002px;width:143px;height:45px;background:var(--sea);color:var(--white);font-size:16px;font-weight:600;text-align:center;line-height:45px}
.news-title{position:absolute;left:649px;top:700px;font-size:21px;font-weight:700;color:var(--sea)}
.news-title span{color:var(--gold)}
.news{position:absolute;left:649px;width:452px;display:flex;gap:24px}
.news .thumb{flex:none;width:166px;height:128px;background:var(--white);padding:3px;box-shadow:0 0 3px rgba(0,0,0,.2)}
.news .thumb div{width:100%;height:100%}
.news h3{font-size:13.5px;font-weight:600;line-height:20px;color:var(--ink)}
.news p{font-size:12px;line-height:19px;color:var(--muted);margin-top:6px}
.news a{display:block;margin-top:10px;color:var(--sea);font-size:13.5px;font-weight:600;text-decoration:none}
.footer{position:absolute;left:0;top:1092px;width:1200px;height:72px;background:var(--sea);color:var(--white);font-size:12.5px}
.footer .copy{position:absolute;left:100px;top:27px}
.footer .follow{position:absolute;right:99px;top:20px;display:flex;align-items:center;gap:9px}
.footer .follow span{margin-right:2px}
.social{width:29px;height:29px;border-radius:50%;border:2px solid var(--white)}
</style>
</head>
<body>
<div class="hero-photo" role="img" aria-label="Underwater photo of a scuba diver waving over a coral reef">
  <div class="diver"></div>
</div>
<div class="page-fade" role="img" aria-label="Faint snowy mountain backdrop"></div>

<div class="brand"><span class="dot"></span>Brinewardsea</div>
<div class="call">
  <span class="ring"><svg width="20" height="20" viewBox="0 0 24 24"><path d="M6.6 10.8c1.4 2.8 3.8 5.1 6.6 6.6l2.2-2.2c.3-.3.7-.4 1-.2 1.1.4 2.3.6 3.6.6.6 0 1 .4 1 1V20c0 .6-.4 1-1 1C10.6 21 3 13.4 3 4c0-.6.4-1 1-1h3.5c.6 0 1 .4 1 1 0 1.3.2 2.5.6 3.6.1.3 0 .7-.2 1z" fill="none" stroke="#e0a52c" stroke-width="1.8"/></svg></span>
  <span>Call Us: <b>(800)-555-0142</b></span>
</div>

<nav class="nav">
  <a>Home</a><a>Brinewardsea</a><a>About Us</a><a>Learn More</a><a>Schedule</a><a>Contact Us</a>
  <span class="lang"><span class="flag"></span><svg width="9" height="6"><path d="M0 0h9L4.5 6z" fill="#fff"/></svg></span>
</nav>

<div class="arrow left"><svg width="18" height="24"><path d="M14 3L5 12l9 9" fill="none" stroke="#1a3a5a" stroke-width="4"/></svg></div>
<div class="arrow right"><svg width="18" height="24"><path d="M4 3l9 9-9 9" fill="none" stroke="rgba(255,255,255,.5)" stroke-width="4"/></svg></div>

<div class="hero-title">BRINEWARDSEA</div>
<div class="hero-sub">CHARTERS AND SCUBA</div>

<form class="search">
  <h2>Search for your dream charter TODAY!</h2>
  <div class="radio"><i></i>I have approximate dates</div>
  <div class="radio on"><i></i>I'm flexible</div>
  <span class="field">First Name:</span>
  <span class="field">Email:</span>
  <span class="btn-gold">Find Charters</span>
</form>

<section class="welcome">
  <h1>Welcome to Our <span>Brinewardsea</span></h1>
  <p class="lead">Nam a ante nec sapien tristique consequat at vel lorem. Etiam rutrum imperdiet justo, et viverra ligula eleifend ut.</p>
  <p>Nullam at rhoncus velit. Duis massa ipsum, hendrerit et faucibus in, facilisis sed lorem. Vestibulum ac ligula vestibulum, rutrum ex vehicula, tempus nisl. Integer mi tortor, maximus quis fringilla a, dictum non ipsum.</p>
  <p>Lorem ipsum dolor sit amet, consectetur adipiscing elit. Fusce semper vitae leo sit amet vehicula. Sed viverra, justo ac consectetur hendrerit, lacus elit tempor urna, gravida mattis lacus ex sed sem. Nam consectetur, arcu in iaculis dapibus, urna felis congue elit, in consectetur nisi massa sed metus. Nullam a tortor ut mauris auctor interdum id vel neque.</p>
</section>
<span class="btn-blue">Read More »</span>

<h2 class="news-title">LATEST <span>NEWS</span></h2>
<article class="news" style="top:754px">
  <div class="thumb"><div role="img" aria-label="Skier descending a snowy slope" style="background:linear-gradient(160deg,#1536b8,#6fa6e8 45%,#f2f6fb 70%)"></div></div>
  <div><h3>Nec appareat definiebas ut, tota assum legimus ea mea.</h3>
  <p>Vestibulum et aliquam velit, sit amet consequat dolor. Nulla tincidunt placerat orci ac varius. Ut maximus eget eros eu gravida.</p>
  <a>Read More ➜</a></div>
</article>
<article class="news" style="top:917px">
  <div class="thumb"><div role="img" aria-label="Group of friends on a sailing yacht deck" style="background:linear-gradient(180deg,#5fa9e0,#2c7fc4 45%,#d9dde2 75%,#b43a3a)"></div></div>
  <div><h3>Caribbean Luxury Yacht Charter</h3>
  <p>A Caribbean luxury yacht charter is the most exclusive and most personalized way to explore the Caribbean. Whether you want to lounge in a top-deck hot tub.</p>
  <a>Read More ➜</a></div>
</article>

<footer class="footer">
  <div class="copy">BRINEWARDSEA. © 2016 | Privacy Policy</div>
  <div class="follow"><span>FOLLOW US :</span>
    <i class="social" style="background:#3b5998"></i>
    <i class="social" style="background:#1da1f2"></i>
    <i class="social" style="background:#c4302b"></i>
    <i class="social" style="background:#dd4b39"></i>
    <i class="social" style="background:#d29a1e"></i>
  </div>
</footer>
</body>
</html>
```